We would like a postcard design for our small medical billing company called Tarvello Medical Billing based in Southern California. We do medical billing for physicians including nephrologist's, and facilities including out patient dialysis centers. We would like a postcard to advertise, and expand our business.

Target Market(s)

Nephrologist's, Physicians, and Dialysis Facilities

Industry/Entity Type

Medical

```html
<!DOCTYPE html>
<html lang="en">
<head>
<meta charset="utf-8">
<title>Tarvello Medical Billing Postcard</title>
<link rel="stylesheet" href="https://fonts.googleapis.com/css2?family=Arimo:wght@400;700&display=swap">
<style>
  :root {
    --olive-text: #86843f;
    --olive-dark: #8a875a;
    --olive-mid: #a6a27a;
    --olive-light: #c9c5a6;
    --ink: #1c1c1c;
    --white: #ffffff;
    --rule: #9a9a9a;
    --photo-light: #f3f5f7;
    --photo-mid: #c9d5df;
    --photo-blue: #7fa6c4;
    --photo-warm: #e2cdb8;
  }
  * { margin: 0; padding: 0; box-sizing: border-box; }
  html, body { width: 747px; height: 1200px; overflow: hidden; background: var(--white); }
  body { font-family: "Arimo", Arial, sans-serif; color: var(--ink); position: relative; }

  .card { position: absolute; left: 0; width: 747px; }
  .card-front { top: 0; height: 578px; }
  .card-back { top: 603px; height: 597px; border: 2px solid var(--rule); }

  .brand-title { position: absolute; color: var(--olive-text); font-weight: 700; font-size: 22.5px; }
  .front-header .brand-title { left: 23px; top: 24px; }
  .front-phone { position: absolute; right: 30px; top: 17px; font-size: 34px; }
  .header-rule { position: absolute; left: 27px; right: 0; top: 66px; height: 2px; background: var(--rule); }

  .photo { position: absolute; }
  .photo-team {
    left: 266px; top: 70px; width: 481px; height: 505px;
    background:
      radial-gradient(ellipse 30% 22% at 72% 28%, var(--photo-warm) 0%, transparent 100%),
      radial-gradient(ellipse 40% 60% at 30% 80%, var(--photo-blue) 0%, transparent 100%),
      linear-gradient(90deg, var(--photo-light) 0%, var(--photo-mid) 45%, var(--white) 75%, var(--photo-mid) 100%);
  }
  .photo-agent-front {
    left: 27px; top: 368px; width: 153px; height: 106px;
    background: linear-gradient(120deg, var(--photo-light), var(--photo-mid) 60%, var(--photo-warm));
  }
  .photo-agent-back {
    left: 356px; top: 88px; width: 118px; height: 170px;
    background: linear-gradient(160deg, var(--photo-light), var(--photo-mid) 60%, var(--photo-warm));
  }

  .headline-panel {
    position: absolute; left: 27px; top: 70px; width: 239px; height: 294px;
    background: linear-gradient(180deg, var(--olive-dark), var(--olive-mid));
    padding: 38px 12px 0 21px;
  }
  .headline { font-size: 21px; font-weight: 700; line-height: 30px; color: var(--ink); }
  .front-web { position: absolute; left: 23px; bottom: 12px; font-size: 14px; color: var(--ink); }

  .address-block {
    position: absolute; left: 27px; top: 474px; width: 239px; height: 101px;
    background: var(--white); padding: 9px 0 0 19px; font-size: 14px; line-height: 1.45; font-style: normal;
  }

  .slogan-band {
    position: absolute; left: 284px; top: 394px; width: 463px; height: 61px;
    background: var(--olive-mid); display: flex; align-items: center; padding-left: 8px;
    font-size: 17px; font-weight: 700; color: var(--ink); letter-spacing: 0.2px;
  }

  .card-back .brand-title { left: 21px; top: 52px; }
  .benefits-panel {
    position: absolute; left: 0; top: 88px; width: 356px; height: 170px;
    background: linear-gradient(180deg, var(--olive-dark), var(--olive-mid));
    padding: 17px 0 0 10px; list-style: none;
  }
  .benefits-panel li { color: var(--white); font-weight: 700; font-size: 15.5px; line-height: 22px; }
  .phone-band {
    position: absolute; left: 0; top: 258px; width: 474px; height: 61px;
    background: var(--olive-light); padding: 12px 0 0 10px; font-size: 32px;
  }
  .service-list { position: absolute; top: 340px; list-style: none; font-size: 14px; line-height: 19px; }
  .service-list.col-left { left: 10px; }
  .service-list.col-right { left: 268px; }
  .service-list li { position: relative; padding-left: 22px; }
  .service-list li::before {
    content: ""; position: absolute; left: 0; top: 4px; width: 11px; height: 11px;
    border-radius: 50%; background: var(--olive-dark);
  }
  .back-contact { position: absolute; left: 133px; top: 452px; font-size: 14px; line-height: 19px; }
  .back-contact span { display: block; }
  .back-contact .email { padding-left: 4px; }
</style>
</head>
<body>
  <section class="card card-front">
    <header class="front-header">
      <div class="brand-title">Tarvello Medical Billing Center</div>
      <div class="front-phone">(562) 318-4470</div>
      <div class="header-rule"></div>
    </header>

    <div class="photo photo-team" role="img" aria-label="Smiling physician in white coat with stethoscope, nurses in blue scrubs behind him"></div>

    <div class="headline-panel">
      <h1 class="headline">Fast and Accurate<br>Billing for<br>Physicians and<br>Dialysis Facilities</h1>
      <div class="front-web">www.TarvelloBilling.com</div>
    </div>

    <div class="photo photo-agent-front" role="img" aria-label="Billing specialist wearing a headset at her desk"></div>

    <address class="address-block">
      2185 Harbor Crest Avenue<br>
      Torrance CA 90503<br>
      info@TarvelloBilling.com
    </address>

    <div class="slogan-band">FEWER HEADACHES.&nbsp; INCREASED PROFITABILITY.</div>
  </section>

  <section class="card card-back">
    <div class="brand-title">Tarvello Medical Billing Center</div>

    <ul class="benefits-panel">
      <li>Increased Cash Flow!</li>
      <li>High Reimbursement Rates!</li>
      <li>Claims Usually Processed Within 24 Hours!</li>
      <li>Payments are mailed directly to you!</li>
      <li>No Software or Hardware Costs!</li>
      <li>No Training Costs!</li>
    </ul>

    <div class="photo photo-agent-back" role="img" aria-label="Billing specialist wearing a headset"></div>

    <div class="phone-band">(562) 318-4470</div>

    <ul class="service-list col-left">
      <li>Claim Processing</li>
      <li>Payment Posting</li>
      <li>Follow up Correspondence</li>
      <li>Design Super Bill (charge sheet)</li>
    </ul>
    <ul class="service-list col-right">
      <li>Monthly Aging Report</li>
      <li>Monthly Productivity Report</li>
      <li>Monthly consult meeting</li>
    </ul>

    <div class="back-contact">
      <span class="web">www.TarvelloBilling.com</span>
      <span class="email">info@TarvelloBilling.com</span>
    </div>
  </section>
</body>
</html>
```